Business Card Re-design

We are looking for a fresh bold look for general office business cards. We are a staffing agency that staffs industrial, coal mining, and clerical jobs.
Tag Line: We match the RIGHT talent to the RIGHT roles.
Marrowby Office: 437 W. Hollowmere Ave, Marrowby, IN - 47298
p. 812.555.0183 f. 812.555.0196
Quillmont Office: 926 S. Larkfen Way, Quillmont, IN - 47231
p. 812.555.0127 f. 812.555.0196
Absentee/Emergency 24hr Hotline 812.555.0164 opt.1
www.tallowcrestworkforce.example

```html
<!DOCTYPE html>
<html lang="en">
<head>
<meta charset="utf-8">
<title>Tallowcrest Workforce – Business Cards</title>
<link rel="stylesheet" href="https://fonts.googleapis.com/css2?family=Lato:wght@400;700;900&display=swap">
<style>
  :root {
    --bg: #e9e6e1;
    --ink-black: #0d0e10;
    --ink-black-soft: #24262a;
    --paper: #ffffff;
    --brand-blue: #2f4f8c;
    --brand-sky: #5ea3d9;
    --brand-green: #4ea944;
    --text-light: #e4e6ea;
  }
  * { box-sizing: border-box; margin: 0; padding: 0; }
  html, body { width: 1200px; height: 1024px; overflow: hidden; }
  body {
    background: var(--bg);
    font-family: "Lato", Arial, sans-serif;
    position: relative;
  }
  .card {
    position: absolute;
    left: 194px;
    width: 812px;
    height: 464px;
    border-radius: 6px;
    overflow: hidden;
    box-shadow: 0 10px 24px rgba(0,0,0,.18);
  }
  .card--front { top: 32px; background: var(--ink-black); }
  .card--back {
    top: 528px;
    background: linear-gradient(135deg, var(--ink-black-soft) 0%, var(--ink-black) 55%, #050506 100%);
  }

  .front__paper {
    position: absolute; left: 0; top: 0; width: 100%; height: 200px;
    background: var(--paper);
  }
  .front__stripes { position: absolute; inset: 0; width: 100%; height: 100%; }

  .wordmark { position: absolute; display: flex; align-items: center; gap: 14px; }
  .wordmark__square { width: 22px; height: 22px; background: var(--brand-green); flex: none; }
  .wordmark__name {
    font-weight: 900; color: var(--brand-blue);
    text-transform: uppercase; line-height: 1.0; letter-spacing: .02em;
  }
  .card--front .wordmark { left: 44px; top: 68px; }
  .card--front .wordmark__name { font-size: 30px; }

  .holder { position: absolute; left: 360px; top: 60px; }
  .holder__name {
    font-weight: 900; font-size: 24px; color: var(--brand-blue);
    text-transform: uppercase; letter-spacing: .02em;
  }
  .holder__title { font-size: 15px; font-weight: 700; color: var(--brand-green); margin-top: 4px; }

  .contact {
    position: absolute; left: 44px; top: 226px;
    list-style: none; color: var(--text-light); font-size: 17px;
  }
  .contact li { display: flex; align-items: center; gap: 10px; height: 29px; }
  .contact li.contact__indent { padding-left: 26px; }
  .contact__icon { width: 16px; height: 16px; flex: none; fill: var(--brand-green); }
  .contact__office { color: var(--brand-green); font-weight: 700; }

  .card--back .wordmark {
    left: 50%; top: 150px; transform: translateX(-50%);
  }
  .card--back .wordmark__name { font-size: 54px; color: var(--brand-sky); }
  .card--back .wordmark__square { width: 34px; height: 34px; }
  .back__text {
    position: absolute; left: 0; right: 0; top: 318px;
    text-align: center; color: var(--text-light);
  }
  .back__tagline { font-size: 19px; font-style: italic; }
  .back__web { font-size: 17px; color: var(--brand-green); margin-top: 10px; }
</style>
</head>
<body>

<section class="card card--front" aria-label="Business card front">
  <div class="front__paper"></div>
  <svg class="front__stripes" viewBox="0 0 812 464" aria-hidden="true">
    <defs>
      <linearGradient id="band-blue" x1="0" y1="0" x2="1" y2="1">
        <stop offset="0" stop-color="#2f4f8c"/>
        <stop offset="1" stop-color="#5ea3d9"/>
      </linearGradient>
    </defs>
    <polygon points="570,0 660,0 812,213 812,339" fill="url(#band-blue)"/>
    <polygon points="660,0 692,0 812,168 812,213" fill="#ffffff"/>
    <polygon points="692,0 752,0 812,84 812,168" fill="#4ea944"/>
  </svg>

  <div class="wordmark">
    <span class="wordmark__square"></span>
    <span class="wordmark__name">Tallowcrest<br>Workforce</span>
  </div>

  <div class="holder">
    <p class="holder__name">Dana Whitfield</p>
    <p class="holder__title">VP of Sales &amp; Operations</p>
  </div>

  <ul class="contact">
    <li><svg class="contact__icon" viewBox="0 0 16 16"><path d="M3.5 1 6 3.5 4.6 5.4c.8 1.9 2.2 3.3 4 4.1L10.5 8 15 10.5 13.6 14C7 14 2 9 2 2.4z"/></svg>812.555.0142</li>
    <li><svg class="contact__icon" viewBox="0 0 16 16"><path d="M1 3h14v10H1zm1.5 1.2v.3L8 8.6l5.5-4.1v-.3z"/></svg>dwhitfield@tallowcrestworkforce.example</li>
    <li><svg class="contact__icon" viewBox="0 0 16 16"><circle cx="8" cy="8" r="7"/><circle cx="8" cy="8" r="3" fill="#0d0e10"/></svg>www.tallowcrestworkforce.example</li>
    <li><svg class="contact__icon" viewBox="0 0 16 16"><path d="M8 0a5.5 5.5 0 0 1 5.5 5.5C13.5 10 8 16 8 16S2.5 10 2.5 5.5A5.5 5.5 0 0 1 8 0zm0 3.3a2.2 2.2 0 1 0 0 4.4 2.2 2.2 0 0 0 0-4.4z"/></svg><span class="contact__office">Marrowby Office:</span></li>
    <li class="contact__indent">437 W. Hollowmere Ave, Marrowby, IN - 47298</li>
    <li><svg class="contact__icon" viewBox="0 0 16 16"><path d="M8 0a5.5 5.5 0 0 1 5.5 5.5C13.5 10 8 16 8 16S2.5 10 2.5 5.5A5.5 5.5 0 0 1 8 0zm0 3.3a2.2 2.2 0 1 0 0 4.4 2.2 2.2 0 0 0 0-4.4z"/></svg><span class="contact__office">Quillmont Office:</span></li>
    <li class="contact__indent">926 S. Larkfen Way, Quillmont, IN - 47231</li>
  </ul>
</section>

<section class="card card--back" aria-label="Business card back">
  <div class="wordmark">
    <span class="wordmark__square"></span>
    <span class="wordmark__name">Tallowcrest<br>Workforce</span>
  </div>
  <div class="back__text">
    <p class="back__tagline">We match the RIGHT talent to the RIGHT roles</p>
    <p class="back__web">www.tallowcrestworkforce.example</p>
  </div>
</section>

</body>
</html>
```